Personal Blog

The wordpress blog style and layout should be similar to http://www.ninalofwent.com

homepage: my photo, list of things, call to action then 3 boxes (The Blog, The Book and podcast)

Other pages: About us, Blog, Consulting, Contact

Target Market(s)

Web Marketing Consultant

Industry/Entity Type

Consulting

Colors
3277b5
33a6d7
f04a50
f68e4e
33b7a4

```html
<!DOCTYPE html>
<html lang="en">
<head>
<meta charset="utf-8">
<title>Darian Kelmore — Consulting</title>
<link rel="stylesheet" href="https://fonts.googleapis.com/css2?family=Arimo:ital,wght@0,400;0,700;1,400;1,700&family=Raleway:wght@400;500;700&family=Roboto+Condensed:wght@400;700&display=swap">
<style>
:root{
  --orange:#e0601a;
  --orange-light:#f2792c;
  --ink:#1d1d1d;
  --text:#333333;
  --muted:#5a5a5a;
  --page:#f3f3f1;
  --rule:#d6d6d6;
  --footer:#1f1f1f;
  --footer-bottom:#151515;
  --footer-text:#6f6f6f;
  --white:#ffffff;
}
*{box-sizing:border-box;margin:0;padding:0}
html,body{width:742px;height:1200px;overflow:hidden}
body{position:relative;background:var(--page);font-family:"Arimo",Arial,sans-serif;color:var(--text)}
.abs{position:absolute}

/* hero */
.hero{left:0;top:0;width:742px;height:342px;background:linear-gradient(180deg,#c9d6e2 0%,#dfe6ec 45%,#c7ccd0 75%,#a9aeb2 100%)}
.top-strip{left:0;top:0;width:742px;height:4px;background:#2a2a2a}
.masthead{left:63px;top:0;width:616px;height:70px;background:rgba(255,255,255,.93);border-radius:0 0 9px 9px;box-shadow:0 1px 3px rgba(0,0,0,.25)}
.brand{left:72px;top:26px;display:flex;align-items:center;gap:8px;font-family:"Raleway",sans-serif;font-weight:700;font-size:22px;color:var(--ink)}
.brand-mark{width:14px;height:14px;background:var(--orange);border-radius:2px}
.nav{left:307px;top:31px;display:flex;align-items:center;font-size:9.5px;color:var(--ink)}
.nav a{color:inherit;text-decoration:none;margin-right:23px}
.nav .current{background:var(--orange);color:var(--white);padding:4px 11px;border-radius:4px;margin-right:28px}
.hero-lead{left:63px;top:112px;font-size:14px;line-height:24px;color:var(--ink)}
.hero-lead strong{color:var(--orange);font-size:16px}
.topics{left:63px;top:181px;list-style:none;font-size:10.5px;color:var(--ink)}
.topics li{display:flex;align-items:center;gap:7px;height:24.6px}

/* testimonial */
.divider{left:200px;top:371px;width:342px;height:1px;background:var(--rule)}
.quote-badge{left:358px;top:356px;width:32px;height:32px;border-radius:50%;background:var(--orange)}
.quote-mark{left:74px;top:386px;font-family:Georgia,serif;font-size:44px;color:#c9c9c9;font-style:italic}
.quote-text{left:107px;top:398px;width:570px;font-style:italic;font-size:10.8px;line-height:17.5px;color:var(--muted)}
.quote-cite{left:420px;top:434px;width:236px;text-align:right;font-style:italic;font-weight:700;font-size:8.5px;color:var(--orange)}

/* feature cards */
.feature{top:467px;width:183px;height:212px;background:var(--white);border-top:2px solid var(--orange);border-bottom:2px solid var(--orange);text-align:center}
.feature-icon{width:67px;height:67px;border-radius:50%;background:var(--orange);margin:13px auto 0;display:flex;align-items:center;justify-content:center}
.feature h2{font-family:"Raleway",sans-serif;font-weight:500;font-size:18px;color:var(--ink);margin-top:10px}
.feature p{font-size:8.3px;line-height:12.3px;color:var(--ink);padding:0 12px;margin-top:9px;height:40px}
.button-outline{display:inline-block;margin-top:12px;width:73px;height:23px;line-height:21px;border:1px solid #d2d2d2;border-radius:3px;font-size:10px;color:var(--orange)}

/* recent blogs */
.section-rule{left:250px;top:735px;width:242px;height:1px;background:var(--rule)}
.section-title{left:296px;top:725px;width:150px;background:var(--page);text-align:center;font-family:"Raleway",sans-serif;font-weight:500;font-size:17px;color:var(--ink);letter-spacing:.3px}
.post{top:771px;width:173px;height:222px;background:var(--white)}
.post-image{width:173px;height:120px}
.post h3{font-family:"Roboto Condensed",sans-serif;font-weight:700;font-size:9.5px;line-height:13.5px;color:var(--ink);padding:8px 8px 0;letter-spacing:.2px}
.post p{font-family:"Roboto Condensed",sans-serif;font-size:8px;line-height:11px;color:var(--muted);padding:3px 8px 0}
.button-solid{display:inline-block;margin:10px 0 0 8px;background:var(--orange);color:var(--white);font-family:"Roboto Condensed",sans-serif;font-size:8px;padding:3px 6px}

/* footer */
.footer{left:0;top:1026px;width:742px;height:146px;background:var(--footer)}
.footer h4{position:absolute;top:22px;font-family:"Raleway",sans-serif;font-weight:700;font-size:10px;color:#e8e8e8}
.footer-about{left:87px;top:44px;width:168px;font-size:8px;line-height:12px;color:#585858}
.field{left:287px;width:142px;height:17px;background:var(--white);border:1px solid #ccc;font-size:7.5px;padding:3px 5px;color:var(--ink)}
.join{left:287px;top:103px;width:142px;height:21px;background:linear-gradient(180deg,var(--orange-light),var(--orange));color:var(--white);font-family:"Raleway",sans-serif;font-weight:700;font-size:11.5px;text-align:center;line-height:21px;border-radius:2px}
.contact-row{left:489px;display:flex;gap:9px;font-size:8.3px;line-height:12px;color:#7a7a7a}
.contact-rule{left:489px;width:190px;height:1px;background:#2e2e2e}
.contact-email{color:var(--orange)}
.legal{left:0;top:1172px;width:742px;height:28px;background:var(--footer-bottom);text-align:center;line-height:28px;font-size:8.5px;color:#777}
</style>
</head>
<body>

<div class="abs hero" role="img" aria-label="Photo of a smiling consultant in shirt and red tie typing at a desktop computer, blurred hillside town behind"></div>
<div class="abs top-strip"></div>

<header class="abs masthead"></header>
<div class="abs brand"><span class="brand-mark"></span>Darian Kelmore</div>
<nav class="abs nav">
  <a class="current" href="#">ABOUT</a>
  <a href="#">Blog</a>
  <a href="#">Consulting</a>
  <a href="#">Resources</a>
  <a href="#">Book</a>
  <a href="#">Contact</a>
</nav>

<p class="abs hero-lead">Text ho here &amp; <strong>Product Management</strong><br>text here Online Marketing, to learn topics:</p>
<ul class="abs topics">
  <li><svg width="9" height="9" viewBox="0 0 10 10"><circle cx="5" cy="5" r="5" fill="#e0601a"/><path d="M2.6 5.1l1.7 1.6 3.2-3.3" stroke="#fff" stroke-width="1.4" fill="none"/></svg>Product Management</li>
  <li><svg width="9" height="9" viewBox="0 0 10 10"><circle cx="5" cy="5" r="5" fill="#e0601a"/><path d="M2.6 5.1l1.7 1.6 3.2-3.3" stroke="#fff" stroke-width="1.4" fill="none"/></svg>Customer Development</li>
  <li><svg width="9" height="9" viewBox="0 0 10 10"><circle cx="5" cy="5" r="5" fill="#e0601a"/><path d="M2.6 5.1l1.7 1.6 3.2-3.3" stroke="#fff" stroke-width="1.4" fill="none"/></svg>Digital Marketing</li>
  <li><svg width="9" height="9" viewBox="0 0 10 10"><circle cx="5" cy="5" r="5" fill="#e0601a"/><path d="M2.6 5.1l1.7 1.6 3.2-3.3" stroke="#fff" stroke-width="1.4" fill="none"/></svg>Branding &amp; Reputation</li>
</ul>

<div class="abs divider"></div>
<svg class="abs quote-badge" viewBox="0 0 32 32"><circle cx="16" cy="16" r="16" fill="#e0601a"/><text x="16" y="25" text-anchor="middle" font-family="Georgia,serif" font-weight="700" font-size="22" fill="#fff">”</text></svg>
<div class="abs quote-mark">“</div>
<blockquote class="abs quote-text">"....I was blown away by his breadth of industry knowledge, the straight talking delivery and collaborative format. A highly recommended Social media experts and thought leader..."</blockquote>
<p class="abs quote-cite">-Marco Velden - Marketing</p>

<section class="abs feature" style="left:63px">
  <div class="feature-icon"><svg width="38" height="32" viewBox="0 0 38 32" fill="none" stroke="#fff" stroke-width="2.4"><ellipse cx="15" cy="12" rx="12" ry="9"/><path d="M8 19l-3 6 8-4"/><path d="M27 9c5 1 8 4 8 8 0 3-2 5-4 6l2 5-6-3c-5 1-10-1-11-5"/></svg></div>
  <h2>The Blog</h2>
  <p>simply dummy text of the printing and type-setting industry. Lorem Ipsum has been the industry's standard dummy text ever</p>
  <span class="button-outline">Read More</span>
</section>
<section class="abs feature" style="left:279px">
  <div class="feature-icon"><svg width="32" height="34" viewBox="0 0 32 34" fill="none" stroke="#fff" stroke-width="2.4" stroke-linejoin="round"><path d="M10 3h19l-6 24H4z"/><path d="M4 27c0 3 2 4 4 4h17l5-22"/><path d="M13 10h10M12 15h10"/></svg></div>
  <h2>The Book</h2>
  <p>simply dummy text of the printing and type-setting industry. Lorem Ipsum has been the industry's standard dummy text</p>
  <span class="button-outline">Read More</span>
</section>
<section class="abs feature" style="left:496px">
  <div class="feature-icon"><svg width="36" height="34" viewBox="0 0 36 34" fill="#fff"><circle cx="13" cy="14" r="6"/><path d="M2 32c0-8 5-11 11-11s11 3 11 11z"/><circle cx="27" cy="9" r="7" fill="none" stroke="#fff" stroke-width="1.8"/><rect x="26" y="8" width="2" height="5"/><circle cx="27" cy="5.5" r="1.1"/></svg></div>
  <h2>Consulting</h2>
  <p>simply dummy text of the printing and type-setting industry. Lorem Ipsum has been the industry's standard dummy text</p>
  <span class="button-outline">Read More</span>
</section>

<div class="abs section-rule"></div>
<h2 class="abs section-title">RECENT BLOGS</h2>

<article class="abs post" style="left:71px">
  <div class="post-image" role="img" aria-label="Photo of an open laptop, notebook and coffee cup on a wooden table" style="background:linear-gradient(135deg,#3a2a1e,#8a5a34 55%,#b98a5a)"></div>
  <h3>Yet Another video Post Format With Embedded Media</h3>
  <p>Ipsum is simply dummy text of the printing and typesetting industry. Lorem Ipsum has been the industry's standard</p>
  <span class="button-solid">Watch Video</span>
</article>
<article class="abs post" style="left:287px">
  <div class="post-image" role="img" aria-label="Photo of a desk from above with keyboard, magazines, phone and stationery" style="background:linear-gradient(135deg,#d8c8b8,#c9a98e 50%,#b07a5a)"></div>
  <h3>Yet Another video Post Format With Embedded Media</h3>
  <p>Ipsum is simply dummy text of the printing and typesetting industry. Lorem Ipsum has been the industry's standard</p>
  <span class="button-solid">Watch Video</span>
</article>
<article class="abs post" style="left:498px">
  <div class="post-image" role="img" aria-label="Photo of a person working on a laptop at an outdoor wooden table" style="background:linear-gradient(135deg,#5e4a3a,#2e3238 55%,#1c2026)"></div>
  <h3>Yet Another video Post Format With Embedded Media</h3>
  <p>Ipsum is simply dummy text of the printing and typesetting industry. Lorem Ipsum has been the industry's standard</p>
  <span class="button-solid">Watch Video</span>
</article>

<footer class="abs footer">
  <h4 style="left:87px">About IT Consultants</h4>
  <h4 style="left:285px">Join My New Business</h4>
  <h4 style="left:489px">Contact Us</h4>
  <p class="abs footer-about">Lorem Ipsum is simply dummy text of the printing and typesetting industry. Lorem Ipsum has been the industry's standard dummy text ever since the 1500s, when an unknown printer took a galley of type and scrambled it to make a type specimen book. It has survived not only five centuries,</p>
  <div class="abs field" style="top:46px">Enter Your Name</div>
  <div class="abs field" style="top:77px">Enter Email Name</div>
  <div class="abs join">Join For Free!</div>

  <div class="abs contact-row" style="top:33px"><svg width="9" height="10" viewBox="0 0 10 10" fill="#666"><path d="M5 0a3.5 3.5 0 0 0-3.5 3.5C1.5 6 5 10 5 10s3.5-4 3.5-6.5A3.5 3.5 0 0 0 5 0zm0 5a1.5 1.5 0 1 1 0-3 1.5 1.5 0 0 1 0 3z"/></svg><span>Larkfield Works, Inc.<br>1180 Harbor Row, Suite 210<br>Millbrook, OH 40512</span></div>
  <div class="abs contact-rule" style="top:92px"></div>
  <div class="abs contact-row" style="top:100px"><svg width="9" height="9" viewBox="0 0 10 10" fill="#666"><path d="M2 0l2 2.5-1 1.3c.6 1.3 1.6 2.3 2.9 2.9l1.3-1L10 8l-1.5 2C4 10 0 6 0 1.5z"/></svg><span>(99) 555 010 2468</span></div>
  <div class="abs contact-rule" style="top:118px"></div>
  <div class="abs contact-row" style="top:124px"><svg width="9" height="8" viewBox="0 0 10 8" fill="#666"><path d="M0 0h10v8H0z"/><path d="M0 0l5 4 5-4" stroke="#1f1f1f" fill="none"/></svg><span class="contact-email">hello@kelmore-studio.net</span></div>
  <div class="abs contact-rule" style="top:140px"></div>
</footer>
<div class="abs legal">© 2014 Copyright - Darian Kelmore . All rights reserved</div>

</body>
</html>
```